IT Management and Consulting company wants a design

The website should transfer an innovative, forward-oriented, optimistic, and serious image to my customer. Because we work in an agile, the design should transfer this approach.

The new color should make a serious, but not boring, impression for the business visitors of top-level companies.

The main focus topics are:
* IT strategy consulting
* Digital transformation
* IT quality management

The website should be in the English language.

The website should be created for WordPress. The existing website is http://www.t-vork.com (no WordPress) is provided by servalpin.de. A WordPress sandbox system exists.

Target Market(s)

Purchasing departments, IT decision makers from companies, project recruiting companies

Industry/Entity Type

IT-Provider, Telecommunication, Automotive

Coding

Coded - Design and coding required

Number of Pages Required

4 page

Font styles to use
Serif
Sans Serif

Requirements
Must have
• Long-pager scrolling, a detail page for each portfolio topics, contact page, page about the company
Nice to have
• Parallax animation less is more, maybe a nice Hero Video Header, interessting 3D graph, Isometric graphs will bi nice, more clean than overloaded,
Should not have
• personal recruting page like in www.t-vork.com

```html
<!DOCTYPE html>
<html lang="en">
<head>
<meta charset="utf-8">
<title>Varnholt Consulting</title>
<link href="https://fonts.googleapis.com/css2?family=Roboto:wght@400;500;700;900&family=Open+Sans:ital,wght@0,400;0,600;1,400&display=swap" rel="stylesheet">
<style>
:root{
  --brand:#f2b50a;
  --brand-dark:#c98c00;
  --ink:#444;
  --muted:#777;
  --topbar:#7a7a7a;
  --grey-band:#ececec;
  --cream:#fdf5d8;
  --white:#fff;
}
*{box-sizing:border-box;margin:0;padding:0}
html,body{width:1200px;height:4800px;overflow:hidden;background:var(--white)}
body{font-family:"Open Sans",Arial,sans-serif;color:var(--ink);position:relative}
.site{position:absolute;left:38px;top:120px;width:1125px;border:3px solid #8a8a8a;border-top:0;background:var(--white);box-shadow:0 4px 10px rgba(0,0,0,.12)}
section,header,footer,.topbar{position:relative;width:100%}
.abs{position:absolute}
.label{font-family:Roboto,sans-serif;font-weight:500;font-size:14px;text-decoration:underline;color:var(--ink);letter-spacing:.3px}
.h2{font-family:Roboto,sans-serif;font-weight:900;font-size:29px;line-height:30px;color:#555;text-transform:uppercase}
.body-text{font-size:11.5px;line-height:22px;color:#555;text-align:justify}
.btn{background:var(--brand);color:var(--ink);font-size:10px;display:flex;align-items:center;justify-content:center;border-radius:2px}
/* top bar */
.topbar{height:49px;background:var(--topbar);color:var(--white);font-size:11px;display:flex;align-items:center;justify-content:center;gap:14px}
.topbar span{display:flex;align-items:center;gap:5px}
/* header */
.header{height:79px}
.logo{display:flex;align-items:center;gap:8px}
.logo-name{font-family:Roboto,sans-serif;font-weight:500;font-size:21px;color:#333}
.logo-mark{width:10px;height:10px;background:#333}
.nav{left:430px;top:31px;display:flex;gap:28px;font-size:11.5px;font-family:Roboto,sans-serif;color:#333}
/* hero */
.hero{height:620px;padding:0 9px}
.hero-photo{position:absolute;left:9px;right:9px;top:0;bottom:0;background:linear-gradient(100deg,#8d9aa6 0%,#6f7d89 40%,#4c5864 70%,#3c444d 100%)}
.hero-sub{left:319px;top:232px;font-family:Roboto,sans-serif;color:var(--brand);font-size:22px}
.hero-title{left:319px;top:262px;font-family:Roboto,sans-serif;font-weight:700;color:var(--white);font-size:40px;line-height:50px}
.hero-btn{left:319px;top:381px;width:150px;height:38px;border-radius:19px;border:2px solid var(--brand);background:var(--white);font-size:10px;display:flex;align-items:center;padding-left:22px;color:#333}
.hero-btn i{position:absolute;right:3px;top:3px;width:28px;height:28px;border-radius:50%;background:var(--brand)}
.social-sq{left:84px;width:24px;height:24px;border:1.5px solid var(--brand)}
.dot{top:555px;width:16px;height:16px;border-radius:50%;background:var(--white)}
/* about */
.about{height:876px}
.card{background:var(--cream);text-align:center;padding:42px 14px 0;font-size:11px;line-height:21px;color:#666}
.card h3{font-family:Roboto,sans-serif;font-size:14px;text-decoration:underline;color:#333;margin-bottom:8px}
.circle{border-radius:50%;background:var(--brand);border:3px solid #fff;box-shadow:0 0 0 1px var(--brand)}
/* services */
.services{height:474px;background:var(--grey-band)}
.svc{width:170px;text-align:center;font-family:Roboto,sans-serif;font-size:14px;font-weight:500;line-height:16px;color:#333}
.svc .circle{width:68px;height:68px;margin:0 auto 14px;display:flex;align-items:center;justify-content:center}
/* portfolio */
.portfolio{height:1513px}
.tabs{left:281px;top:300px;display:flex;font-size:11px;font-family:Roboto,sans-serif}
.tabs span{padding:12px 18px;color:#333}
.tabs .active{border:1px solid var(--brand);border-bottom:0;background:#fff;color:var(--brand);position:relative;z-index:2}
.panel{left:131px;top:345px;width:862px;height:1103px;border:1px solid var(--brand)}
.pcard{width:356px;background:#fff;box-shadow:0 0 8px rgba(0,0,0,.06);text-align:center;padding:34px 28px 0}
.pcard .img{height:198px;background:linear-gradient(135deg,#b9c2c9,#6c7781);position:relative}
.pcard .img .circle{position:absolute;left:50%;bottom:-24px;width:48px;height:48px;margin-left:-24px}
.pcard h4{font-family:Roboto,sans-serif;font-size:15px;font-weight:500;color:#222;margin:34px 0 10px}
.pcard p{font-size:11px;line-height:21px;color:#777}
.pcard .btn{width:116px;height:32px;margin:14px auto 0;color:#fff;font-size:11px}
/* testimonials */
.testimonials{height:488px;background:var(--grey-band);text-align:center}
.arrow{top:262px;font-size:26px;color:#999;font-family:Roboto,sans-serif}
/* footer */
.footer{height:343px}
.fcol{top:68px;font-size:11px;color:#555;line-height:34px}
.fcol h5{font-family:Roboto,sans-serif;font-size:13px;font-weight:700;text-decoration:underline;color:#444;line-height:20px;margin-bottom:14px}
.fsoc{top:252px;width:28px;height:28px;border-radius:50%;background:var(--brand);border:2px solid #fff;box-shadow:0 0 0 1px var(--brand)}
</style>
</head>
<body>
<div class="site">

  <div class="topbar">
    <span><svg width="10" height="13" viewBox="0 0 10 13"><path d="M5 0a5 5 0 0 0-5 5c0 4 5 8 5 8s5-4 5-8a5 5 0 0 0-5-5z" fill="#f2b50a"/><circle cx="5" cy="5" r="2" fill="#7a7a7a"/></svg>Varnholt Consulting GmbH Werkstraße 12 - 14 D-80331 Feldkirchen</span>
    <span><svg width="11" height="11" viewBox="0 0 12 12"><path d="M2 1l2 0 1 3-1.5 1a7 7 0 0 0 3.5 3.5L8 7l3 1v2a1 1 0 0 1-1 1A9 9 0 0 1 1 2a1 1 0 0 1 1-1z" fill="#f2b50a"/></svg>+49 (0) 8100 4417720</span>
    <span><svg width="12" height="12" viewBox="0 0 12 12"><rect x="1" y="3" width="10" height="8" fill="#f2b50a"/><rect x="3" y="1" width="6" height="3" fill="#f2b50a"/></svg>+49 (0) 8100 4417729</span>
    <span><svg width="14" height="10" viewBox="0 0 14 10"><rect width="14" height="10" fill="#f2b50a"/><path d="M0 0l7 6 7-6" stroke="#7a7a7a" fill="none"/></svg>info@t-vork.com</span>
  </div>

  <header class="header">
    <div class="abs logo" style="left:37px;top:27px">
      <div class="logo-mark"></div>
      <div class="logo-name">Varnholt Consulting</div>
    </div>
    <nav class="abs nav"><span>Home</span><span>About Us</span><span>Services ▾</span><span>Portfolio ▾</span><span>Contact Us</span></nav>
    <div class="abs btn" style="left:935px;top:19px;width:171px;height:34px;font-size:10.5px;gap:50px"><span>Get In Touch</span><span>»</span></div>
  </header>

  <section class="hero">
    <div class="hero-photo" role="img" aria-label="Business team reviewing charts on a laptop in a bright office"></div>
    <div class="abs social-sq" style="top:259px"></div>
    <div class="abs social-sq" style="top:299px"></div>
    <div class="abs social-sq" style="top:339px"></div>
    <div class="abs hero-sub">Welcome To Varnholt Consulting GmbH</div>
    <div class="abs hero-title">We Create The Best<br>Conditions For IT Systems</div>
    <div class="abs hero-btn">CONTACT US<i></i></div>
    <div class="abs dot" style="left:84px"></div>
    <div class="abs dot" style="left:112px"></div>
    <div class="abs dot" style="left:140px;background:var(--brand)"></div>
    <div class="abs dot" style="left:168px"></div>
    <div class="abs dot" style="left:196px"></div>
  </section>

  <section class="about">
    <div class="abs label" style="left:126px;top:160px">ABOUT US</div>
    <div class="abs h2" style="left:126px;top:192px;width:380px">Welcome To Varnholt<br>Consulting GmbH</div>
    <p class="abs body-text" style="left:126px;top:262px;width:380px">Lorem ipsum dolor sit amet, consectetur adipiscing elit, sed do eiusmod tempor incididunt ut labore et dolore magna aliqua. Vulputate dignissim suspendisse in est ante. Faucibus turpis in eu mi bibendum neque. Sodales ut etiam sit amet nisl purus. Velit laoreet id donec ultrices tincidunt.</p>
    <div class="abs" style="left:148px;top:406px;font-size:10.5px;color:var(--brand-dark)">Read More ➜</div>
    <div class="abs" style="left:623px;top:96px;width:377px;height:424px;border:3px double var(--brand)"></div>
    <div class="abs" role="img" aria-label="Colleagues gathered around a laptop discussing a project" style="left:596px;top:71px;width:364px;height:411px;background:linear-gradient(135deg,#c9c4bd,#8f8477 60%,#5d564f);box-shadow:0 10px 24px rgba(0,0,0,.15)"></div>

    <div class="abs card" style="left:146px;top:551px;width:182px;height:194px"><h3>Mission</h3>Our mission is to carry out complex projects efficiently with high quality for the benefit of our customers. Transparent, reliable, agile</div>
    <div class="abs card" style="left:358px;top:551px;width:182px;height:194px"><h3>Vission</h3>Our mission is to carry out complex projects efficiently with high quality for the benefit of our customers. Transparent, reliable, agile</div>
    <div class="abs circle" style="left:200px;top:510px;width:74px;height:74px"></div>
    <div class="abs circle" style="left:412px;top:510px;width:74px;height:74px"></div>
    <div class="abs btn" style="left:131px;top:772px;width:160px;height:34px">Know More About Us »</div>

    <div class="abs" role="img" aria-label="Portrait of the founder" style="left:613px;top:577px;width:76px;height:76px;border-radius:50%;background:linear-gradient(#bfc6cc,#5a6570)"></div>
    <div class="abs" style="left:596px;top:663px;width:110px;text-align:center;font-size:10px;color:#444;line-height:15px">Lukas Varnholt<br><span style="color:#999">Founder</span></div>
    <div class="abs" style="left:703px;top:566px;width:249px;height:156px;background:var(--cream);font-style:italic;font-size:11px;line-height:18px;color:#666;text-align:center;padding:16px 16px">"Thanks to more than 25 years of activity in project management and consulting, mainly for medium-sized and large companies, Varnholt Consulting is very familiar with the challenges in all project phases of complex IT projects."</div>
  </section>

  <section class="services">
    <div class="abs label" style="left:131px;top:70px">SERVICES</div>
    <div class="abs h2" style="left:131px;top:98px">Solutions We Offer!</div>
    <p class="abs body-text" style="left:131px;top:146px;width:380px">Lorem ipsum dolor sit amet, consectetur adipiscing elit, sed do eiusmod tempor incididunt ut labore et dolore magna aliqua. Vulputate dignissim suspendisse in est ante. Faucibus turpis in eu mi bibendum neque. Sodales ut etiam sit amet nisl purus. Velit laoreet id donec ultrices tincidunt.</p>
    <div class="abs btn" style="left:131px;top:292px;width:120px;height:34px">Our Services »</div>

    <div class="abs svc" style="left:515px;top:73px"><div class="circle"><svg width="30" height="30" viewBox="0 0 30 30" fill="none" stroke="#444" stroke-width="1.6"><circle cx="10" cy="9" r="4"/><circle cx="20" cy="9" r="4"/><path d="M3 26v-6a7 7 0 0 1 14 0v6M13 26v-6a7 7 0 0 1 14 0v6"/></svg></div>IT Strategy<br>Consulting</div>
    <div class="abs svc" style="left:672px;top:73px"><div class="circle"><svg width="30" height="30" viewBox="0 0 30 30" fill="none" stroke="#444" stroke-width="1.6"><path d="M8 14a6 6 0 0 1 11-4 5 5 0 0 1 4 9H8a4 4 0 0 1 0-5z"/><rect x="6" y="21" width="6" height="5"/><rect x="18" y="21" width="6" height="5"/></svg></div>Digital<br>Transformation</div>
    <div class="abs svc" style="left:830px;top:73px"><div class="circle"><svg width="30" height="30" viewBox="0 0 30 30" fill="none" stroke="#444" stroke-width="1.6"><circle cx="17" cy="12" r="7"/><path d="M14 19v4h6v-4M4 24l5-5"/><circle cx="7" cy="10" r="3"/></svg></div>IT Quality<br>Management</div>
    <div class="abs svc" style="left:515px;top:245px"><div class="circle"><svg width="30" height="30" viewBox="0 0 30 30" fill="none" stroke="#444" stroke-width="1.6"><rect x="7" y="4" width="16" height="22"/><path d="M11 10h8M11 15h8M11 20h5"/></svg></div>Project<br>Management</div>
    <div class="abs svc" style="left:672px;top:245px"><div class="circle"><svg width="30" height="30" viewBox="0 0 30 30" fill="none" stroke="#444" stroke-width="1.6"><rect x="5" y="5" width="20" height="20" rx="2"/><path d="M9 11h12M9 16h12M9 21h7"/></svg></div>Test Management</div>
    <div class="abs svc" style="left:830px;top:245px"><div class="circle"><svg width="30" height="30" viewBox="0 0 30 30" fill="none" stroke="#444" stroke-width="1.6"><rect x="5" y="4" width="14" height="20"/><circle cx="19" cy="18" r="5"/><path d="M23 22l4 4"/></svg></div>Commissioning<br>Management</div>
  </section>

  <section class="portfolio">
    <div class="abs label" style="left:0;width:100%;text-align:center;top:70px">PORTFOLIO</div>
    <div class="abs h2" style="left:0;width:100%;text-align:center;top:98px">Varnholt Consulting Specializes In Complex Projects</div>
    <p class="abs body-text" style="left:131px;top:146px;width:862px;font-size:11px">Our range of services covers the management of the entire development process from applications and extensions to quality assurance through to going live and support afterwards.</p>
    <p class="abs body-text" style="left:131px;top:200px;width:862px;font-size:11px">Varnholt Consulting specializes in complex projects in heterogeneous IT environments. We deliver in high quality. We work with the necessary procedural models to achieve customer satisfaction and project success. We bring a reasonable degree of pragmatism and approach things optimistically without losing sight of reality. We master difficult situations.</p>
    <div class="abs tabs"><span class="active">Projects In Excellence</span><span>Consulting In Excellence</span><span>Digitalization</span><span>Cloud Transition</span></div>
    <div class="abs panel"></div>

    <div class="abs pcard" style="left:191px;top:420px;height:446px">
      <div class="img" role="img" aria-label="Team working at computers in an office"><div class="circle"></div></div>
      <h4>Excellent Project Management</h4>
      <p>Excellent project management: We manage projects according to the PMCB Competence Baseline of an international project framework, according</p>
      <div class="btn">✓ Learn more</div>
    </div>
    <div class="abs pcard" style="left:578px;top:420px;height:446px">
      <div class="img" role="img" aria-label="Colleagues reviewing documents at a desk"><div class="circle"></div></div>
      <h4>Excellent Quality</h4>
      <p>Defects recognized late are expensive. We carry out quality assurance of software in an integrated environment according to the TQSB® standard and set up environments for</p>
      <div class="btn">✓ Learn more</div>
    </div>
    <div class="abs pcard" style="left:191px;top:922px;height:431px">
      <div class="img" role="img" aria-label="Meeting table seen from above with people and papers"><div class="circle"></div></div>
      <h4>Excellent Commissioning</h4>
      <p>Going live with applications in complex IT environments requires far more than just deploying them in a productive environment. Neighboring systems</p>
      <div class="btn">✓ Learn more</div>
    </div>
    <div class="abs pcard" style="left:578px;top:922px;height:431px">
      <div class="img" role="img" aria-label="Two colleagues looking at a laptop"><div class="circle"></div></div>
      <h4>Excellent Service For Regular Operations</h4>
      <p>Varnholt Consulting defines and establishes the necessary processes on the basis of the ITSM best internship proposals or improves them together with our client. How</p>
      <div class="btn">✓ Learn more</div>
    </div>
  </section>

  <section class="testimonials">
    <div class="abs label" style="left:0;width:100%;top:68px">TESTIMONIALS</div>
    <div class="abs h2" style="left:0;width:100%;top:96px">Check What Our Clients Say</div>
    <div class="abs" role="img" aria-label="Portrait of the client" style="left:517px;top:171px;width:90px;height:90px;border-radius:50%;border:3px solid #333;background:linear-gradient(#b8a99a,#4d4038)"></div>
    <div class="abs arrow" style="left:128px">‹</div>
    <div class="abs arrow" style="left:985px">›</div>
    <p class="abs" style="left:250px;top:280px;width:625px;font-size:11.5px;line-height:23px;color:#444">I am slide content. Click edit button to change this text. Lorem ipsum dolor sit amet, consectetur adipiscing elit. Ut elit tellus, luctus nec ullamcorper mattis, pulvinar dapibus leo.</p>
    <div class="abs" style="left:0;width:100%;top:344px;font-family:Roboto,sans-serif;font-size:17px;color:#222">MARK OLSEN</div>
    <div class="abs" style="left:0;width:100%;top:370px;font-size:9px;color:#aaa">DESIGNER</div>
    <div class="abs" style="left:0;width:100%;top:390px;font-size:12px;color:#999;letter-spacing:4px">• • •</div>
  </section>

  <footer class="footer">
    <div class="abs logo" style="left:131px;top:80px">
      <div class="logo-mark"></div>
      <div class="logo-name">Varnholt Consulting</div>
    </div>
    <p class="abs body-text" style="left:131px;top:130px;width:205px;font-size:11px">Lorem ipsum dolor sit amet, consectetur adipiscing elit. Ut elit tellus, luctus nec ullamcorper mattis, pulvinar dapibus leo.</p>
    <div class="abs fsoc" style="left:157px"></div>
    <div class="abs fsoc" style="left:197px"></div>
    <div class="abs fsoc" style="left:237px"></div>
    <div class="abs fsoc" style="left:277px"></div>

    <div class="abs fcol" style="left:351px"><h5>Our Company</h5>Who We Are<br>About Company<br>Services We Provide<br>What We Have Done</div>
    <div class="abs fcol" style="left:514px"><h5>Important Links</h5>Home<br>About Us<br>Services ▾<br>Portfolio ▾<br>Contact Us</div>
    <div class="abs fcol" style="left:669px;width:140px;line-height:16px"><h5>Our Services</h5><div style="margin-bottom:14px">IT strategy consulting</div><div style="margin-bottom:14px">Digital<br>transformation</div><div>IT quality<br>management</div></div>
    <div class="abs fcol" style="left:833px;width:160px;line-height:22px"><h5>Our Contacts</h5>
      <div style="display:flex;gap:8px"><span style="color:var(--brand);padding-top:22px">●</span><span>Varnholt Consulting GmbH Werkstraße 12 - 14 D-80331 Feldkirchen</span></div>
      <div style="margin-top:8px"><span style="color:var(--brand)">✆</span> +49 (0) 8100 4417720</div>
      <div><span style="color:var(--brand)">■</span> +49 (0) 8100 4417729</div>
      <div><span style="color:var(--brand)">✉</span> info@t-vork.com</div>
    </div>
  </footer>

</div>
</body>
</html>
```